Web Design for "Global Broadcasting Service Business"

We are a satellite company launching a new exciting brand by the name of "Pelumo". Pelumo is a broadcasting solution provider that gives end-to-end solutions to TV channels and other content providers to deliver and distribute their content globally. Weather it be TV channels that need to be broadcasted in their local regions or internationally, or its collection of news from various locations, or even coverage of special sports or other events, we provide the technology and services to make that happen. This allows the broadcaster to focus on the content rather than worry about the logistics of how it will get to its viewers. We can help place their content to regional cable and satellite operators. Moreover we can provide services for content creation and coverage of major sports, news and special events. Pelumo is one-stop-shop for all broadcast solutions

We want a 20 page static website. I am mentioning certain key competitors of ours so that you can have a look at the comparable look we are anticipating in the design

www.orvenmedia.tv
www.dunharlow.com
www.pembrick.com

Its a global company so the design has to give the same look and feel

Target Market(s)

TV Channel Owners and their Technical Heads

Industry/Entity Type

Business

Requirements
Must have
• We want the designers to submit the home page design first giving us the look and feel of the website design. you can use sample text and any satellite based image to start off. Once we shortlist the best home page designs we will ask you to create the remaining pages.

The most work is on the home page, remaining subsections will only require a change in text and images at most. the overall look and feel of the website including headers and footers will remain the same

```html
<!DOCTYPE html>
<html lang="en">
<head>
<meta charset="utf-8">
<title>Pelumo — Regional Solution, Global Distribution</title>
<link rel="stylesheet" href="https://fonts.googleapis.com/css2?family=Source+Sans+3:wght@400;600;700&family=Montserrat:wght@400;500;600&family=Arimo:wght@400;700&display=swap">
<style>
  :root {
    --white: #ffffff;
    --ink: #1a1a1a;
    --nav-grey: #555555;
    --link-blue: #27a9e1;
    --heading-blue: #1a7ac0;
    --learn-blue: #1f2a8c;
    --brand-red: #c4122f;
    --hero-slate: #3e5561;
    --panel-bg: #e8e1e4;
    --panel-border: #2a7fc0;
    --field-bg: #f2f2f2;
    --field-border: #6a2a4a;
    --button-blue: #00aeef;
    --footer-bg: #595866;
    --footer-text: #e6e6ea;
  }
  * { margin: 0; padding: 0; box-sizing: border-box; }
  html, body { width: 1200px; height: 788px; overflow: hidden; background: var(--white); }
  .page { position: relative; width: 1200px; height: 788px; font-family: "Arimo", Arial, sans-serif; color: var(--ink); }

  .site-header { position: absolute; left: 0; top: 0; width: 1200px; height: 117px; border-bottom: 3px solid var(--brand-red); }
  .brand { position: absolute; left: 184px; top: 22px; }
  .brand-name { display: flex; align-items: center; gap: 8px; font-family: "Source Sans 3", sans-serif; font-weight: 700; font-size: 50px; line-height: 58px; color: var(--ink); letter-spacing: -1px; }
  .brand-dot { width: 12px; height: 12px; border-radius: 50%; background: var(--brand-red); }
  .brand-tagline { font-family: "Source Sans 3", sans-serif; font-size: 10px; color: var(--ink); margin-top: 3px; margin-left: 6px; }

  .utility-nav { position: absolute; right: 205px; top: 22px; display: flex; gap: 12px; font-family: "Source Sans 3", sans-serif; font-size: 13px; }
  .utility-nav a { color: var(--link-blue); text-decoration: none; }
  .main-nav { position: absolute; right: 205px; top: 71px; display: flex; gap: 12px; font-family: "Source Sans 3", sans-serif; font-size: 13.5px; }
  .main-nav a { color: var(--nav-grey); text-decoration: none; }

  .hero { position: absolute; left: 0; top: 120px; width: 1200px; height: 285px; background: var(--hero-slate); }
  .hero-image { position: absolute; left: 167px; top: 0; width: 866px; height: 285px;
    background: linear-gradient(180deg, #8aa0ac 0%, #c9c2b4 22%, #f2cf9c 50%, #f6c46a 78%, #f0b030 100%); }

  .intro { position: absolute; left: 173px; top: 434px; width: 500px; }
  .intro-title { font-family: "Source Sans 3", sans-serif; font-weight: 400; font-size: 19px; color: var(--heading-blue); letter-spacing: 0.2px; }
  .intro-text { margin-top: 16px; font-size: 11.8px; line-height: 22px; color: var(--ink); }
  .learn-more { display: inline-block; margin-top: 11px; font-weight: 700; font-size: 12px; color: var(--learn-blue); text-decoration: none; }

  .newsletter { position: absolute; left: 717px; top: 421px; width: 260px; height: 263px; background: var(--panel-bg); border: 1px solid var(--panel-border); }
  .newsletter-title { position: absolute; left: 16px; top: 17px; font-family: "Montserrat", sans-serif; font-weight: 400; font-size: 18px; color: var(--heading-blue); }
  .field-label { position: absolute; left: 22px; font-size: 11.5px; color: var(--ink); }
  .field-label.username { top: 56px; }
  .field-label.password { top: 130px; }
  .field-input { position: absolute; left: 21px; width: 184px; height: 30px; background: var(--field-bg); border: 1px solid var(--field-border); }
  .field-input.username { top: 82px; }
  .field-input.password { top: 151px; }
  .login-button { position: absolute; left: 21px; top: 195px; width: 96px; height: 32px; background: var(--button-blue); border: 2px solid var(--white); border-radius: 2px; color: var(--white); font-family: "Montserrat", sans-serif; font-weight: 600; font-size: 13px; display: flex; align-items: center; justify-content: center; }
  .register-link { position: absolute; left: 128px; top: 206px; font-weight: 700; font-size: 10.5px; color: var(--heading-blue); text-decoration: none; }

  .site-footer { position: absolute; left: 0; top: 756px; width: 1200px; height: 32px; background: var(--footer-bg); color: var(--footer-text); font-size: 10px; letter-spacing: 0.4px; display: flex; align-items: center; justify-content: center; }
</style>
</head>
<body>
<div class="page">
  <header class="site-header">
    <div class="brand">
      <div class="brand-name"><span class="brand-dot"></span>Pelumo</div>
      <div class="brand-tagline">Regional Solution, Global Distribution</div>
    </div>
    <nav class="utility-nav">
      <a href="#">Global Network</a>
      <a href="#">Beams</a>
    </nav>
    <nav class="main-nav">
      <a href="#">Home</a>
      <a href="#">Who We Are</a>
      <a href="#">Broadcast Solutions</a>
      <a href="#">Regional Distribution</a>
      <a href="#">On-Demand Services</a>
    </nav>
  </header>

  <section class="hero">
    <div class="hero-image" role="img" aria-label="Satellite dish silhouetted against a golden sunset sky"></div>
  </section>

  <section class="intro">
    <h1 class="intro-title">REGINAL SOLUTION&nbsp; I&nbsp; GLOBAL DISTRIBUTION</h1>
    <p class="intro-text">Lorem ipsum dolor sit amet, consectetur adipisicing elit, sed do eiusmod tempor incididunt ut labore et dolore magna aliqua. Ut enim ad minim veniam, quis nostrud exercitation ullamco laboris nisi ut aliquip ex ea commodo consequat. Duis aute irure dolor in reprehenderit in voluptate velit esse cillum dolore eu fugiat nulla pariatur. Excepteur sint occaecat cupidatat non proident, sunt in culpa qui officia deserunt mollit anim id est laborum.</p>
    <a class="learn-more" href="#">Learn more....</a>
  </section>

  <aside class="newsletter">
    <h2 class="newsletter-title">Signup for Newsletter</h2>
    <span class="field-label username">Username</span>
    <div class="field-input username"></div>
    <span class="field-label password">Password</span>
    <div class="field-input password"></div>
    <div class="login-button">Login</div>
    <a class="register-link" href="#">Register</a>
  </aside>

  <footer class="site-footer">© 2014 Pelumo</footer>
</div>
</body>
</html>
```